Winter is coming, is your home ready ?

We are a full service Insulation contracting services company . We insulate new and existing homes, commercial and industrial buildings.

We are looking for a billboard that shows our harsh winter approaching and a call to action for getting a free estimate.

We specialize in spray foam insulation but it doesn't need to be called out on the billboard if too much text make it looks too busy.

We do enjoy humor if its something that could work and keep people thinking of us.
Company web site is www.brivalhomeseal.com
Company phone number is 555-318-2976

```html
<!DOCTYPE html>
<html lang="en">
<head>
<meta charset="utf-8">
<title>Brival Home Seal – Winter Billboard</title>
<link href="https://fonts.googleapis.com/css2?family=Anton&family=Oswald:wght@400;500&family=Arimo:wght@400;700&display=swap" rel="stylesheet">
<style>
  :root {
    --page: #ffffff;
    --mist-light: #f4f4f4;
    --mist-mid: #dcdcdc;
    --charcoal: #2e2e2f;
    --slate: #6c6d70;
    --lime: #adbf33;
    --photo-dark: #3b3832;
    --photo-warm: #c9924a;
    --shadow-grey: #9a9a9a;
  }
  html, body {
    margin: 0;
    padding: 0;
    width: 1200px;
    height: 1200px;
    overflow: hidden;
    background: var(--page);
  }
  .billboard { display: block; width: 1200px; height: 1200px; }
  .headline-grey { font-family: 'Anton', sans-serif; fill: var(--slate); }
  .headline-lime { font-family: 'Anton', sans-serif; fill: var(--lime); }
  .headline-shadow { font-family: 'Anton', sans-serif; fill: var(--charcoal); }
  .we-insulate { font-family: 'Anton', sans-serif; fill: var(--charcoal); letter-spacing: 2px; }
  .service-item { font-family: 'Oswald', sans-serif; font-weight: 500; fill: var(--charcoal); }
  .cta-text { font-family: 'Anton', sans-serif; fill: #ffffff; }
  .phone { font-family: 'Arimo', sans-serif; font-weight: 700; fill: var(--charcoal); }
  .web { font-family: 'Arimo', sans-serif; font-weight: 700; fill: var(--charcoal); letter-spacing: 1.5px; }
  .brand-name { font-family: 'Oswald', sans-serif; font-weight: 400; fill: var(--slate); }
</style>
</head>
<body>
<svg class="billboard" viewBox="0 0 1200 1200" xmlns="http://www.w3.org/2000/svg">
  <defs>
    <linearGradient id="mistBand" x1="0" y1="0" x2="1" y2="0">
      <stop offset="0" stop-color="#d6d6d6"/>
      <stop offset="0.35" stop-color="#f2f2f2"/>
      <stop offset="0.7" stop-color="#ececec"/>
      <stop offset="1" stop-color="#d9d9d9"/>
    </linearGradient>
    <linearGradient id="mistStrip" x1="0" y1="0" x2="1" y2="0">
      <stop offset="0" stop-color="#dedede"/>
      <stop offset="0.5" stop-color="#f5f5f5"/>
      <stop offset="1" stop-color="#e0e0e0"/>
    </linearGradient>
    <radialGradient id="cabinScene" cx="0.7" cy="0.75" r="0.8">
      <stop offset="0" stop-color="var(--photo-warm)"/>
      <stop offset="0.35" stop-color="#6f6353"/>
      <stop offset="0.7" stop-color="var(--photo-dark)"/>
      <stop offset="1" stop-color="#a9abab"/>
    </radialGradient>
  </defs>

  <!-- misty forest band -->
  <rect role="img" aria-label="Misty snowy pine forest background" x="0" y="390" width="1200" height="297" fill="url(#mistBand)"/>
  <rect x="0" y="687" width="1200" height="108" fill="var(--page)"/>
  <rect role="img" aria-label="Misty forest strip" x="0" y="795" width="1200" height="15" fill="url(#mistStrip)"/>

  <!-- headline -->
  <text class="headline-shadow" x="111" y="474" font-size="78" textLength="490" lengthAdjust="spacingAndGlyphs">Winter is Coming!</text>
  <text class="headline-grey" x="109" y="472" font-size="78" textLength="490" lengthAdjust="spacingAndGlyphs">Winter is Coming!</text>
  <text class="headline-shadow" x="627" y="474" font-size="78" textLength="524" lengthAdjust="spacingAndGlyphs">Is Your Home Ready</text>
  <text class="headline-lime" x="625" y="472" font-size="78" textLength="524" lengthAdjust="spacingAndGlyphs">Is Your Home Ready</text>
  <text class="headline-lime" x="1150" y="468" font-size="104">?</text>

  <!-- cabin photo -->
  <rect x="106" y="491" width="398" height="288" rx="20" fill="var(--shadow-grey)"/>
  <rect role="img" aria-label="Log cabin in a snowy misty forest with warm glowing windows" x="96" y="483" width="399" height="288" rx="20" fill="url(#cabinScene)"/>

  <!-- services -->
  <text class="we-insulate" x="566" y="552" font-size="68" textLength="310" lengthAdjust="spacingAndGlyphs">We insulate</text>
  <g class="service-list">
    <polygon points="894,498 904,505 894,512" fill="var(--charcoal)"/>
    <text class="service-item" x="907" y="513" font-size="22" textLength="226" lengthAdjust="spacingAndGlyphs">New and Existing Homes,</text>
    <polygon points="894,521 904,528 894,535" fill="var(--charcoal)"/>
    <text class="service-item" x="907" y="536" font-size="22" textLength="202" lengthAdjust="spacingAndGlyphs">Commercial Buildings</text>
    <polygon points="894,544 904,551 894,558" fill="var(--charcoal)"/>
    <text class="service-item" x="907" y="559" font-size="22" textLength="190" lengthAdjust="spacingAndGlyphs">Industrial Buildings.</text>
  </g>

  <!-- call to action -->
  <rect x="614" y="582" width="124" height="126" rx="8" fill="var(--lime)"/>
  <g transform="rotate(-3 676 645)">
    <text class="cta-text" x="620" y="626" font-size="26">Get</text>
    <text class="cta-text" x="621" y="659" font-size="26">Free</text>
    <text class="cta-text" x="622" y="693" font-size="26" textLength="112" lengthAdjust="spacingAndGlyphs">Estimate!</text>
  </g>
  <polygon points="755,601 779,625 755,649" fill="var(--slate)"/>

  <!-- contact box -->
  <rect x="796" y="582" width="334" height="89" rx="14" fill="var(--page)" stroke="var(--lime)" stroke-width="3"/>
  <text class="phone" x="811" y="634" font-size="46" textLength="306" lengthAdjust="spacingAndGlyphs">555-318-2976</text>
  <text class="web" x="812" y="659" font-size="19" textLength="303" lengthAdjust="spacingAndGlyphs">www.brivalhomeseal.com</text>

  <!-- brand -->
  <rect x="886" y="704" width="22" height="22" fill="var(--slate)"/>
  <text class="brand-name" x="918" y="725" font-size="26" textLength="200" lengthAdjust="spacingAndGlyphs">Brival Home Seal, Inc.</text>
</svg>
</body>
</html>
```